依頼概要
毎年、全社員の名前、顔写真、誕生日、ひと言コメントを掲載した冊子を作成しています。これまでは表紙について、自社でデザインを実施していましたがロゴ等を並列のするのみのデザイン性に乏しいものでした。
この名鑑を社員一人一人が手にしたときに、ワクワクする!すぐに読みたい!テンションがUPする!というようなデザインにしたいと考えています。
スピード重視ですので、あまり凝ったデザインでなくても良いかなと考えています。

なお、名鑑は2法人(社会福祉法人光彩苑と学校法人桐谷学園)で共同で使用いたします。

法人の理念は、
For The Community~地域のために私たちができること~

となります。

法人のイメージカラーは、オレンジと緑です。

素晴らしいご提案を頂戴できるように楽しみにしています。

```html
<!DOCTYPE html>
<html lang="ja">
<head>
<meta charset="UTF-8">
<title>スタッフ名鑑'16 — For the Community</title>
<link href="https://fonts.googleapis.com/css2?family=Noto+Sans+JP:wght@500;700;900&family=Roboto:wght@500;700&display=swap" rel="stylesheet">
<style>
  :root {
    --green: #1fb24a;
    --green-dark: #169a3c;
    --orange: #f5a623;
    --white: #ffffff;
    --forest-light: #c9b98a;
    --forest-mid: #6d7a3e;
    --forest-dark: #2e3a1c;
  }
  * { margin: 0; padding: 0; box-sizing: border-box; }
  html, body { width: 846px; height: 1200px; overflow: hidden; background: var(--white); }
  .cover {
    position: relative;
    width: 846px;
    height: 1200px;
    background: var(--white);
    font-family: "Noto Sans JP", sans-serif;
    overflow: hidden;
  }
  .cover-head {
    position: absolute; left: 0; top: 0;
    width: 846px; height: 282px;
    background: var(--green);
    color: var(--white);
  }
  .motto {
    position: absolute; left: 56px; top: 8px;
    font-family: "Roboto", sans-serif;
    font-weight: 500;
    font-size: 100px;
    line-height: 92px;
    letter-spacing: -1px;
    white-space: nowrap;
  }
  .motto-sub {
    position: absolute; left: 58px; top: 210px;
    font-size: 23px;
    font-weight: 700;
    letter-spacing: 1px;
  }
  .org-mark {
    position: absolute; right: 60px; top: 222px;
    display: flex; align-items: center; gap: 8px;
    font-family: "Roboto", sans-serif;
    font-weight: 700;
    font-size: 32px;
    color: var(--white);
  }
  .org-mark .dot {
    width: 22px; height: 22px; border-radius: 50%;
    background: var(--orange);
  }
  .forest-photo {
    position: absolute; left: 0; top: 282px;
    width: 846px; height: 568px;
    background:
      radial-gradient(ellipse at 78% 18%, #f3e6b8 0%, rgba(243,230,184,0) 45%),
      linear-gradient(180deg, var(--forest-light) 0%, var(--forest-mid) 45%, var(--forest-dark) 100%);
  }
  .title-band {
    position: absolute; left: 0; top: 502px;
    width: 846px; height: 226px;
    background: var(--orange);
    color: var(--white);
  }
  .title {
    position: absolute; left: 58px; top: 34px;
    font-size: 96px;
    font-weight: 500;
    line-height: 1.1;
    letter-spacing: -1px;
    white-space: nowrap;
  }
  .corporations {
    position: absolute; left: 486px; top: 156px;
    font-size: 22px;
    font-weight: 700;
    line-height: 34px;
  }
  .facilities {
    position: absolute; left: 0; top: 880px;
    width: 846px; height: 240px;
  }
  .facility-row {
    display: flex; justify-content: space-around; align-items: center;
    padding: 0 36px;
    height: 120px;
  }
  .facility {
    display: flex; align-items: center; gap: 6px;
    font-size: 22px; font-weight: 700;
    color: var(--green-dark);
  }
  .facility .mark {
    width: 16px; height: 16px; border-radius: 50%;
    background: var(--orange);
  }
  .cover-foot {
    position: absolute; left: 0; bottom: 0;
    width: 846px; height: 58px;
    background: var(--green);
  }
</style>
</head>
<body>
<main class="cover">
  <header class="cover-head">
    <h1 class="motto">For<br>the Community</h1>
    <p class="motto-sub">地域のために私たちができること</p>
    <div class="org-mark"><span class="dot"></span>Koseien</div>
  </header>

  <div class="forest-photo" role="img" aria-label="木漏れ日が差し込む森の写真"></div>

  <section class="title-band">
    <h2 class="title">スタッフ名鑑“16</h2>
    <p class="corporations">社会福祉法人光彩苑<br>学校法人桐谷学園</p>
  </section>

  <section class="facilities">
    <div class="facility-row">
      <span class="facility"><span class="mark"></span>陽だまり館</span>
      <span class="facility"><span class="mark"></span>陽だまり苑</span>
      <span class="facility"><span class="mark"></span>若葉の森</span>
      <span class="facility"><span class="mark"></span>ひかり保育園</span>
    </div>
    <div class="facility-row">
      <span class="facility"><span class="mark"></span>みどりの森保育園</span>
      <span class="facility"><span class="mark"></span>和心</span>
      <span class="facility"><span class="mark"></span>そよかぜ</span>
      <span class="facility"><span class="mark"></span>hinata</span>
    </div>
  </section>

  <footer class="cover-foot"></footer>
</main>
</body>
</html>
```